Website for software company "velmor"

We need a website for our software company/startup named "velmor". We are developing several products (currently 3 standard-software products) which are all in different sectors, but all our products are available for Laptops/PC/Mobile Phones/Tablets, ... We do also create custom software and support our customers with consulting to optimize their processes.
We already have a Logo which you can find in the attached files.
We are a young team of 4 members (two founders and 2 employees).

To get an idea of our products -> the first one is a planning software for healthcare organizations (eg. HelpWing, firebrigade, pharmacy), the second one is a booking software for sport clubs and the third one is a competition software for sports hunting. You see very diverse. Include or ignore this info of our products as you like.

The design has to be a bootstrap 4 (or higher) design. We have licenced FontAwesome as iconset. Responsive design should come without saying.

• Starting page, product pages, news section, contact, team, services

```html
<!DOCTYPE html>
<html lang="en">
<head>
<meta charset="utf-8">
<title>Velmor Software</title>
<link rel="stylesheet" href="https://fonts.googleapis.com/css2?family=Poppins:wght@400;500;600;700;800&family=Merriweather:wght@700&display=swap">
<style>
:root{
  --orange:#f47b2a;
  --orange-soft:#f68a3e;
  --ink:#111111;
  --text:#555555;
  --white:#ffffff;
  --line:#333333;
  --shade:rgba(40,40,40,.72);
}
*{box-sizing:border-box;margin:0;padding:0}
html,body{width:1200px;height:3025px;overflow:hidden}
body{position:relative;font-family:"Poppins",sans-serif;color:var(--ink);background:var(--white)}
.abs{position:absolute}
a{color:inherit;text-decoration:none}

/* header */
.topbar{left:517px;top:0;width:683px;height:49px;background:var(--orange);clip-path:polygon(0 0,100% 0,100% 100%,34px 100%);z-index:3;color:#fff;font-size:13px;display:flex;align-items:center;gap:30px;padding-left:50px}
.topbar span{display:flex;align-items:center;gap:8px}
.topbar .socials{display:flex;gap:8px;margin-left:4px}
.topbar .socials i{width:20px;height:20px;border-radius:50%;background:#fff;display:block}
.navbar{left:517px;top:49px;width:683px;height:50px;background:#fff;clip-path:polygon(34px 0,100% 0,100% 100%,0 100%);z-index:3;display:flex;align-items:center;gap:38px;padding-left:51px;font-size:13.5px;font-weight:700}
.brand{left:96px;top:27px;z-index:3;display:flex;align-items:center;gap:12px}
.brand i{width:22px;height:44px;background:var(--orange);display:block}
.brand b{font-size:54px;font-weight:700;color:#333;letter-spacing:1px;line-height:1}

/* hero */
.hero{left:0;top:0;width:1200px;height:784px;background:linear-gradient(135deg,#8a9aa8 0%,#3a4a58 35%,#1f2a33 60%,#7a6a5a 100%)}
.hero-box{left:161px;top:223px;width:878px;height:329px;background:var(--shade);text-align:center;color:#fff}
.hero-box .welcome{font-family:"Merriweather",serif;font-size:29px;margin-top:48px}
.hero-box h1{font-size:64px;font-weight:800;line-height:1;margin-top:6px;letter-spacing:.5px}
.hero-box p{font-size:13.5px;line-height:21px;margin:22px auto 0;width:620px}
.btn{background:var(--orange);color:#fff;font-weight:700;display:flex;align-items:center;justify-content:center}
.hero-box .btn{width:142px;height:42px;margin:20px auto 0;font-size:15px}
.dots{left:1100px;top:356px;display:flex;flex-direction:column;gap:7px}
.dots i{width:12px;height:12px;border:1.5px solid var(--orange);border-radius:50%;display:block}
.dots i.on{background:var(--orange)}

/* products */
.products{left:161px;top:680px;width:878px;height:387px;background:#fff;box-shadow:0 2px 10px rgba(0,0,0,.12)}
.product{top:20px;width:269px;height:347px}
.product .label{position:absolute;left:12px;right:12px;bottom:17px;height:53px;background:#fff;color:var(--orange);font-size:19px;font-weight:700;display:flex;align-items:center;justify-content:center}

/* about */
.about-photo{left:101px;top:1150px;width:539px;height:430px;background:#fff;box-shadow:0 2px 10px rgba(0,0,0,.15);padding:7px}
.about-photo div{width:100%;height:100%;background:linear-gradient(150deg,#d9dee2,#8d9aa3 50%,#c9c3ba)}
.h2{font-size:35px;font-weight:800;line-height:1}
.h2 em{font-style:normal;color:var(--orange)}
.about-title{left:675px;top:1175px}
.about-text{left:675px;top:1224px;width:430px;font-size:12px;line-height:20px;color:var(--text)}
.about-text p+p{margin-top:20px}
.about .btn{left:675px;top:1409px;width:143px;height:44px;font-size:15px}
.feature{top:1494px;width:174px;height:112px;background:#fff;box-shadow:0 2px 10px rgba(0,0,0,.12);text-align:center;font-size:15px;font-weight:700}
.feature svg{display:block;margin:14px auto 8px}

/* testimonials */
.clients{left:0;top:1720px;width:1200px;height:570px;background:linear-gradient(180deg,var(--orange-soft),var(--orange));clip-path:polygon(0 0,100% 0,100% 100%,50% 84.4%,0 100%)}
.clients-title{left:0;top:1790px;width:1200px;text-align:center;color:#fff;font-size:35px}
.clients-sub{left:300px;top:1848px;width:600px;text-align:center;color:#fff;font-size:13px;line-height:21px}
.quote{top:1913px;width:426px;height:206px;background:#fff;border-radius:5px;padding:28px 30px}
.quote p{font-size:11.5px;line-height:19px;color:var(--text)}
.person{display:flex;align-items:center;gap:13px;margin-top:14px}
.avatar{width:62px;height:62px;border-radius:50%;background:linear-gradient(160deg,#c9b7a6,#6a5a50)}
.person b{display:block;color:var(--orange);font-size:16px;font-weight:700}
.person small{font-size:12px;color:var(--ink)}
.arrow{top:1990px}

/* contact */
.contact-title{left:0;top:2290px;width:1200px;text-align:center}
.contact-sub{left:275px;top:2352px;width:650px;text-align:center;font-size:13px;line-height:21px;color:var(--text)}
.info{left:133px;display:flex;gap:20px;align-items:center}
.info .ic{width:47px;height:47px;background:var(--orange);display:flex;align-items:center;justify-content:center}
.info b{display:block;font-size:15px;font-weight:700}
.info span{font-size:13px;color:var(--text);line-height:19px}
.field{left:486px;width:283px;height:50px;border:1.5px solid var(--line);font-size:13px;padding:18px 24px 0}
.message{left:787px;top:2428px;width:283px;height:176px;border:1.5px solid var(--line);font-size:13px;padding:18px 24px}
.submit{left:787px;top:2618px;width:283px;height:50px;font-size:15px}

/* footer */
.footer{left:0;top:2747px;width:1200px;height:278px;background:#000;clip-path:polygon(0 0,50% 86px,100% 0,100% 100%,0 100%)}
.foot-h{color:#fff;font-size:25px;font-weight:700;top:2862px}
.foot-links{left:101px;top:2916px;display:flex;gap:62px;color:#fff;font-size:15px;font-weight:500}
.copy{left:101px;top:2956px;color:#fff;font-size:13.5px}
.join{left:832px;top:2914px;width:270px;height:41px;background:#fff;display:flex}
.join span{flex:1;font-size:13px;padding:12px 18px}
.join b{width:110px;background:var(--orange);color:#fff;font-size:15px;display:flex;align-items:center;justify-content:center;border:2px solid #fff}
.foot-social{left:966px;top:2977px;display:flex;gap:14px}
.foot-social i{width:24px;height:24px;background:#fff;border-radius:4px;display:block}
</style>
</head>
<body>

<div class="abs hero" role="img" aria-label="Photo of developers working together at computer monitors"></div>

<header>
  <div class="abs brand"><i></i><b>VELMOR</b></div>
  <div class="abs topbar">
    <span><svg width="14" height="14" viewBox="0 0 24 24" fill="#fff"><path d="M6.6 10.8a15 15 0 0 0 6.6 6.6l2.2-2.2c.3-.3.7-.4 1-.2 1.1.4 2.3.6 3.6.6.6 0 1 .4 1 1V20c0 .6-.4 1-1 1A17 17 0 0 1 3 4c0-.6.4-1 1-1h3.5c.6 0 1 .4 1 1 0 1.3.2 2.5.6 3.6.1.3 0 .7-.2 1z"/></svg>+9 555 210 7788</span>
    <span><svg width="16" height="12" viewBox="0 0 16 12" fill="none" stroke="#fff" stroke-width="1.5"><rect x="1" y="1" width="14" height="10"/><path d="M1 1l7 6 7-6"/></svg>info@velmor.com</span>
    <span><svg width="14" height="15" viewBox="0 0 14 15" fill="none" stroke="#fff" stroke-width="1.4"><circle cx="7" cy="4.5" r="3.5"/><path d="M1 14.5c0-3.5 2.7-5.5 6-5.5s6 2 6 5.5"/></svg>Login Here</span>
    <div class="socials"><i></i><i></i><i></i></div>
  </div>
  <nav class="abs navbar"><a>HOME</a><a>ABOUT US</a><a>OUR SERVICES</a><a>SHOP</a><a>FAQ</a><a>CONTACT</a></nav>
</header>

<section class="abs hero-box">
  <div class="welcome">welcome to</div>
  <h1>VELMOR SOFTWARE</h1>
  <p>Lorem ipsum dolor sit amet, consectetur adipiscing elit, sed do eiusmod tempor incididunt ut labore et dolore magna aliqua. Quis ipsum suspendisse ultrices gravida.</p>
  <a class="btn">GET STARTED</a>
</section>
<div class="abs dots"><i class="on"></i><i></i><i></i><i></i></div>

<section class="abs products">
  <div class="abs product" style="left:20px;background:linear-gradient(160deg,#cfe2ee,#5f8fae 60%,#2e4a5e)" role="img" aria-label="Photo of a hospital operating room">
    <div class="label">HEALTHCARE</div></div>
  <div class="abs product" style="left:305px;background:linear-gradient(160deg,#8a6a50,#b8262a 55%,#5a1a1a)" role="img" aria-label="Photo of young football players hugging">
    <div class="label">SPORT CLUBS</div></div>
  <div class="abs product" style="left:590px;background:linear-gradient(160deg,#3e4a32,#6a5a3a 50%,#2a2e2a)" role="img" aria-label="Photo of a shooter at an outdoor range">
    <div class="label">SPORTS HUNTING</div></div>
</section>

<section class="about">
  <div class="abs about-photo"><div role="img" aria-label="Photo of a young team working at desks in an office"></div></div>
  <h2 class="abs h2 about-title">ABOUT <em>US</em></h2>
  <div class="abs about-text">
    <p>Lorem ipsum dolor sit amet, consectetur adipiscing elit, sed do eiusmod tempor incididunt ut labore et dolore magna aliqua. Quis ipsum suspendisse ultrices gravida. Risus commodo viverra maecenas accumsan lacus vel facilisis.</p>
    <p>Lorem ipsum dolor sit amet, consectetur adipiscing elit, sed do eiusmod tempor incididunt ut labore et dolore magna aliqua. Quis ipsum suspendisse ultrices gravida. Risus commodo</p>
  </div>
  <a class="abs btn">READ MORE</a>

  <div class="abs feature" style="left:318px">
    <svg width="80" height="54" viewBox="0 0 80 54" fill="none" stroke="#f47b2a" stroke-width="2"><rect x="7" y="2" width="66" height="44" rx="2"/><path d="M1 50h78"/></svg>LAPTOPS</div>
  <div class="abs feature" style="left:512px">
    <svg width="64" height="54" viewBox="0 0 64 54" fill="none" stroke="#f47b2a" stroke-width="2"><rect x="2" y="2" width="60" height="40" rx="2"/><rect x="7" y="7" width="50" height="30"/><path d="M26 42v8M38 42v8M20 51h24"/></svg>PC</div>
  <div class="abs feature" style="left:706px">
    <svg width="60" height="54" viewBox="0 0 60 54" fill="none" stroke="#f47b2a" stroke-width="2"><rect x="18" y="2" width="24" height="48" rx="3"/><circle cx="34" cy="28" r="6"/><path d="M4 16h8M4 26h8M4 36h8M48 14h8M48 40h8"/></svg>MOBILE PHONES</div>
  <div class="abs feature" style="left:899px">
    <svg width="44" height="54" viewBox="0 0 44 54" fill="none" stroke="#f47b2a" stroke-width="2"><rect x="4" y="2" width="36" height="50" rx="4"/><rect x="9" y="9" width="26" height="36"/><circle cx="22" cy="48" r="1"/></svg>TABLETS</div>
</section>

<section>
  <div class="abs clients" role="img" aria-label="Orange tinted photo of a modern office interior"></div>
  <h2 class="abs h2 clients-title">HAPPY CLIENTS SAYS</h2>
  <p class="abs clients-sub">Lorem ipsum dolor sit amet, consectetur adipiscing elit, sed do eiusmod tempor incididunt ut labore et dolore magna aliqua. Quis ipsum suspendisse ultrices gravida.</p>
  <svg class="abs arrow" style="left:98px" width="18" height="28" viewBox="0 0 18 28" fill="none" stroke="#fff" stroke-width="3"><path d="M15 2L3 14l12 12"/></svg>
  <svg class="abs arrow" style="left:1084px" width="18" height="28" viewBox="0 0 18 28" fill="none" stroke="#fff" stroke-width="3"><path d="M3 2l12 12L3 26"/></svg>
  <div class="abs quote" style="left:161px">
    <p>“ Lorem ipsum dolor sit amet, consectetur adipiscing elit, sed do eiusmod tempor incididunt ut labore et dolore magna aliqua. Quis ipsum suspendisse ultrices gravida. Risus commodo viverra maecenas accumsan lacus vel facilisis.......”</p>
    <div class="person"><div class="avatar" role="img" aria-label="Client portrait"></div><div><b>Lena Hartwig</b><small>Position Name</small></div></div>
  </div>
  <div class="abs quote" style="left:613px">
    <p>“ Lorem ipsum dolor sit amet, consectetur adipiscing elit, sed do eiusmod tempor incididunt ut labore et dolore magna aliqua. Quis ipsum suspendisse ultrices gravida. Risus commodo viverra maecenas accumsan lacus vel facilisis.......”</p>
    <div class="person"><div class="avatar" role="img" aria-label="Client portrait"></div><div><b>Nora Feld</b><small>Position Name</small></div></div>
  </div>
</section>

<section>
  <h2 class="abs h2 contact-title">GET IN <em>TOUCH</em></h2>
  <p class="abs contact-sub">Lorem ipsum dolor sit amet, consectetur adipiscing elit, sed do eiusmod tempor incididunt ut labore et dolore magna aliqua. Quis ipsum suspendisse ultrices gravida.</p>

  <div class="abs info" style="top:2421px"><div class="ic"><svg width="18" height="24" viewBox="0 0 18 24" fill="#fff"><path d="M9 0a9 9 0 0 0-9 9c0 7 9 15 9 15s9-8 9-15a9 9 0 0 0-9-9zm0 13a4 4 0 1 1 0-8 4 4 0 0 1 0 8z"/></svg></div><span>453 Street Name, Place Name,<br>City Name - 87650</span></div>
  <div class="abs info" style="top:2489px"><div class="ic"><svg width="22" height="22" viewBox="0 0 24 24" fill="#fff"><path d="M6.6 10.8a15 15 0 0 0 6.6 6.6l2.2-2.2c.3-.3.7-.4 1-.2 1.1.4 2.3.6 3.6.6.6 0 1 .4 1 1V20c0 .6-.4 1-1 1A17 17 0 0 1 3 4c0-.6.4-1 1-1h3.5c.6 0 1 .4 1 1 0 1.3.2 2.5.6 3.6.1.3 0 .7-.2 1z"/></svg></div><div><b>CALL ON</b><span>+1 555 301 4420</span></div></div>
  <div class="abs info" style="top:2558px"><div class="ic"><svg width="22" height="16" viewBox="0 0 22 16" fill="none" stroke="#fff" stroke-width="1.8"><rect x="1" y="1" width="20" height="14"/><path d="M1 1l10 8 10-8"/></svg></div><div><b>EMAIL AT</b><span>info@velmor.com</span></div></div>
  <div class="abs info" style="top:2627px"><div class="ic"><svg width="22" height="22" viewBox="0 0 22 22" fill="none" stroke="#fff" stroke-width="1.6"><circle cx="11" cy="11" r="9.5"/><ellipse cx="11" cy="11" rx="4" ry="9.5"/><path d="M1.5 11h19M3 6h16M3 16h16"/></svg></div><div><b>VISIT US</b><span>www.velmor.com</span></div></div>

  <div class="abs field" style="top:2428px">First Name</div>
  <div class="abs field" style="top:2491px">Last Name</div>
  <div class="abs field" style="top:2555px">Phone Number</div>
  <div class="abs field" style="top:2618px">Email Address</div>
  <div class="abs message">Your Message Goes Here.........</div>
  <a class="abs btn submit">SUBMIT NOW</a>
</section>

<footer>
  <div class="abs footer"></div>
  <h3 class="abs foot-h" style="left:101px">QUICK LINKS</h3>
  <nav class="abs foot-links"><a>HOME</a><a>ABOUT US</a><a>OUR SERVICES</a><a>GALLERY</a><a>CONTACT US</a></nav>
  <p class="abs copy">Copyright © 2022 &nbsp;Velmor Software . All Rights Reserved.</p>
  <h3 class="abs foot-h" style="left:832px">JOIN WITH US</h3>
  <div class="abs join"><span>Email Address</span><b>SUBSCRIBE</b></div>
  <div class="abs foot-social"><i></i><i></i><i></i><i></i></div>
</footer>

</body>
</html>
```